Wendlemoor Vapes labels

We need a label designed for our e-liquid that we will be selling from our store. (E-liquid is used in electronic cigarettes) The label should be 1-1.5 inches tall and ~3 inches long.

Try to focus on highlighting the name brand over the specific flavor.

Bottle size will be 15ml clear bottles.

There will be 10+ flavors and each flavor will need a slightly different label (with the same overall theme) and different nicotine levels varying from 0mg, 6mg, 12mg, and 18mg.

Initial favor list is:
Coral Drift
Velvet Slosh
Tart Currants
Crakle Plums
Papaya Riot
Zingy Drops
Amber Gryphon
Fizzleleaf
Emberlash
Orvin
Nutmeg Twist

Please add the following warning in caps and small font:

(WHITE FONT)
This product contains nicotine or was produced at a facility that processes nicotine which has been known to cause birth defects and other reproductive harm. This product also contains VG/PG and artificial flavors. Not for sale to minors.
(RED FONT)
Toxic if swallowed or has contact with skin. Keep locked up and out of reach of children and pets. In case of accident or you feel unwell seek medical advice immediately.

young adults

Electronic

```html
<!DOCTYPE html>
<html lang="en">
<head>
<meta charset="utf-8">
<title>Wendlemoor Vapes – Velvet Slosh labels</title>
<link href="https://fonts.googleapis.com/css2?family=Oswald:wght@300;500&display=swap" rel="stylesheet">
<style>
  :root {
    --page: #ffffff;
    --black-label: #060708;
    --plum-label: #2d1747;
    --white-label: #ffffff;
    --band-purple: #833f9b;
    --stripe-dark: #4f2570;
    --ribbon-dark: #5a2d86;
    --ribbon-light: #8f45a2;
    --ribbon-back: #3f1e66;
    --brand-blue: #3a7bd0;
    --mark-grey: #b9bcc4;
    --warn-orchid: #8b3c93;
    --warn-plum: #5d3679;
    --warn-red: #e6233d;
    --text-white: #ffffff;
    --text-dark: #222222;
  }
  html, body {
    margin: 0;
    padding: 0;
    width: 1000px;
    height: 1200px;
    overflow: hidden;
    background: var(--page);
  }
  .sheet {
    position: relative;
    width: 1000px;
    height: 1200px;
    font-family: "Oswald", "Arial Narrow", sans-serif;
  }
  .label {
    position: absolute;
    left: 161px;
    width: 678px;
    height: 338px;
    overflow: hidden;
    box-sizing: border-box;
  }
  .label--black { top: 57px; background: var(--black-label); }
  .label--plum  { top: 436px; background: var(--plum-label); }
  .label--white { top: 815px; background: var(--white-label); border: 1px solid #3a3a3a; }

  .warning {
    position: absolute;
    top: 0;
    height: 338px;
    width: 62px;
    box-sizing: border-box;
    padding: 10px 0;
    writing-mode: vertical-rl;
    transform: rotate(180deg);
    font-weight: 300;
    font-size: 10.4px;
    line-height: 19px;
    letter-spacing: 0.05px;
  }
  .warning--left  { left: 17px; }
  .warning--right { left: 573px; }
  .label--black .warning--left { color: var(--warn-orchid); }
  .label--plum  .warning--left { color: var(--warn-plum); }
  .label--white .warning--left { color: var(--warn-red); }
  .label--black .warning--right,
  .label--plum  .warning--right { color: var(--text-white); }
  .label--white .warning--right { color: var(--text-dark); }

  .nicotine-band {
    position: absolute;
    left: 82px;
    top: 0;
    width: 43px;
    height: 338px;
    background: var(--band-purple);
    display: flex;
    align-items: center;
    justify-content: center;
  }
  .nicotine-band span {
    writing-mode: vertical-rl;
    transform: rotate(180deg);
    color: var(--text-white);
    font-weight: 300;
    font-size: 19px;
    white-space: nowrap;
    margin-bottom: 30px;
  }

  .edge-stripe {
    position: absolute;
    left: 550px;
    top: 0;
    height: 338px;
    width: 16px;
    background: linear-gradient(to right, var(--stripe-dark) 0 7px, var(--band-purple) 7px 16px);
  }

  .brand {
    position: absolute;
    left: 229px;
    top: 34px;
    width: 200px;
    text-align: center;
    color: var(--brand-blue);
    font-weight: 500;
  }
  .brand__dot {
    display: block;
    width: 110px;
    height: 110px;
    margin: 0 auto 22px;
    border-radius: 50%;
    background: var(--mark-grey);
  }
  .brand__name {
    display: block;
    font-size: 25px;
    line-height: 30px;
    letter-spacing: 0.5px;
  }
  .brand__sub {
    display: block;
    font-size: 14px;
    line-height: 18px;
    letter-spacing: 9px;
    margin-left: 9px;
  }

  .flavour-ribbon {
    position: absolute;
    left: 217px;
    top: 272px;
    width: 224px;
    height: 50px;
  }
  .flavour-ribbon svg { position: absolute; inset: 0; }
  .flavour-ribbon span {
    position: absolute;
    inset: 0;
    display: flex;
    align-items: center;
    justify-content: center;
    color: var(--text-white);
    font-weight: 300;
    font-size: 22px;
    letter-spacing: 0.3px;
  }
</style>
</head>
<body>
<main class="sheet">

  <!-- Label variant: black -->
  <section class="label label--black">
    <p class="warning warning--left">This product contains nicotine or was produced at a facility that processes nicotine which has been known to cause birth defects and other reproductive harm. This product also contains VG/PG and artificial flavors. Not for sale to minors.</p>
    <div class="nicotine-band"><span>Nicotine by volume: 0mg/mL</span></div>
    <div class="brand">
      <span class="brand__dot"></span>
      <span class="brand__name">WENDLEMOOR</span>
      <span class="brand__sub">VAPES</span>
    </div>
    <div class="flavour-ribbon">
      <svg viewBox="0 0 224 50" width="224" height="50" aria-hidden="true">
        <polygon points="0,8 24,25 0,42 40,48 40,2" fill="var(--ribbon-back)"/>
        <polygon points="224,8 200,25 224,42 184,48 184,2" fill="var(--ribbon-back)"/>
        <polygon points="8,10 112,4 112,46 8,40 24,25" fill="var(--ribbon-dark)"/>
        <polygon points="216,10 112,4 112,46 216,40 200,25" fill="var(--ribbon-light)"/>
      </svg>
      <span>VELVET SLOSH</span>
    </div>
    <div class="edge-stripe"></div>
    <p class="warning warning--right">This product contains nicotine or was produced at a facility that processes nicotine which has been known to cause birth defects and other reproductive harm. This product also contains VG/PG and artificial flavors. Not for sale to minors.</p>
  </section>

  <!-- Label variant: plum -->
  <section class="label label--plum">
    <p class="warning warning--left">This product contains nicotine or was produced at a facility that processes nicotine which has been known to cause birth defects and other reproductive harm. This product also contains VG/PG and artificial flavors. Not for sale to minors.</p>
    <div class="nicotine-band"><span>Nicotine by volume: 0mg/mL</span></div>
    <div class="brand">
      <span class="brand__dot"></span>
      <span class="brand__name">WENDLEMOOR</span>
      <span class="brand__sub">VAPES</span>
    </div>
    <div class="flavour-ribbon">
      <svg viewBox="0 0 224 50" width="224" height="50" aria-hidden="true">
        <polygon points="0,8 24,25 0,42 40,48 40,2" fill="var(--ribbon-back)"/>
        <polygon points="224,8 200,25 224,42 184,48 184,2" fill="var(--ribbon-back)"/>
        <polygon points="8,10 112,4 112,46 8,40 24,25" fill="var(--ribbon-dark)"/>
        <polygon points="216,10 112,4 112,46 216,40 200,25" fill="var(--ribbon-light)"/>
      </svg>
      <span>VELVET SLOSH</span>
    </div>
    <div class="edge-stripe"></div>
    <p class="warning warning--right">This product contains nicotine or was produced at a facility that processes nicotine which has been known to cause birth defects and other reproductive harm. This product also contains VG/PG and artificial flavors. Not for sale to minors.</p>
  </section>

  <!-- Label variant: white -->
  <section class="label label--white">
    <p class="warning warning--left">This product contains nicotine or was produced at a facility that processes nicotine which has been known to cause birth defects and other reproductive harm. This product also contains VG/PG and artificial flavors. Not for sale to minors.</p>
    <div class="nicotine-band"><span>Nicotine by volume: 0mg/mL</span></div>
    <div class="brand">
      <span class="brand__dot"></span>
      <span class="brand__name">WENDLEMOOR</span>
      <span class="brand__sub">VAPES</span>
    </div>
    <div class="flavour-ribbon">
      <svg viewBox="0 0 224 50" width="224" height="50" aria-hidden="true">
        <polygon points="0,8 24,25 0,42 40,48 40,2" fill="var(--ribbon-back)"/>
        <polygon points="224,8 200,25 224,42 184,48 184,2" fill="var(--ribbon-back)"/>
        <polygon points="8,10 112,4 112,46 8,40 24,25" fill="var(--ribbon-dark)"/>
        <polygon points="216,10 112,4 112,46 216,40 200,25" fill="var(--ribbon-light)"/>
      </svg>
      <span>VELVET SLOSH</span>
    </div>
    <div class="edge-stripe"></div>
    <p class="warning warning--right">This product contains nicotine or was produced at a facility that processes nicotine which has been known to cause birth defects and other reproductive harm. This product also contains VG/PG and artificial flavors. Not for sale to minors.</p>
  </section>

</main>
</body>
</html>
```